Business Card for Quillmark Ledger - A cannabis publication for executives.

I'd like some business cards for Quillmark Ledger. The logo is done (great job!) and I need a card design I will use with PRINTLY. I made it a short project to allow time for printing before an event. These will be standard sized cards (final artwork size 3.66" x 2.16" at 300dpi) with a final card size of 3.5" x 2.0". (See PRINTLY.com if you need more info.) I might try rounded corners but am not sure yet. I think the design will work okay with rounded.

Quillmark Ledger will be a bi-weekly publication for the cannabis industry. It is targeted to investors and industry executives, not consumers or pot smokers. So our market is more B2B. However I am open to creativity and making the card something people remark on.

My contact for card:

Dana Merrow
Founder/CEO
dana@quillmarkledger.example

2740 Harlow Avenue
Boston MA 02135
(617)555-0194

Target Market(s)

Executives, Industry people and investors in the Cannabis sector.

Contact Information for Business Card

PRINTLY does do double sided and the second side can be the same or different images. Only one side is required but use of the second side would be a bonus.

Font styles to use
Serif
Sans Serif
Decorative

Colors

Designer to choose colors to be used in the design.

Requirements
Must have
• Logo, contact info
Nice to have
• Style and design to make the card stand out in a crowd.

```html
<!DOCTYPE html>
<html lang="en">
<head>
<meta charset="utf-8">
<title>Quillmark Ledger — Business Card</title>
<link rel="stylesheet" href="https://fonts.googleapis.com/css2?family=Montserrat:wght@500;600;700;800&display=swap">
<style>
  :root {
    --backdrop: #eef1f7;
    --card: #fbfbfb;
    --ink: #1c1c1c;
    --brand-blue: #1771ba;
    --brand-green: #79ad2f;
  }
  * { box-sizing: border-box; margin: 0; padding: 0; }
  html, body { width: 1200px; height: 1200px; overflow: hidden; }
  body {
    background: var(--backdrop);
    font-family: "Montserrat", Arial, sans-serif;
    color: var(--ink);
    position: relative;
  }
  .card {
    position: absolute;
    left: 180px;
    width: 840px;
    height: 480px;
    background: var(--card);
    box-shadow: 0 6px 18px rgba(30, 40, 70, 0.18);
    overflow: hidden;
  }
  .card--front { top: 90px; }
  .card--back { top: 630px; }
  .card__bands { position: absolute; inset: 0; width: 840px; height: 480px; }

  .contact-name {
    position: absolute;
    right: 60px;
    top: 62px;
    font-size: 64px;
    font-weight: 800;
    letter-spacing: -1px;
    line-height: 1;
    white-space: nowrap;
  }
  .contact-title {
    position: absolute;
    right: 60px;
    top: 138px;
    font-size: 30px;
    font-weight: 700;
    line-height: 1;
    white-space: nowrap;
  }
  .contact-email {
    position: absolute;
    left: 60px;
    top: 196px;
    display: flex;
    align-items: center;
    gap: 16px;
    font-size: 16px;
    font-weight: 500;
    white-space: nowrap;
  }
  .contact-address {
    position: absolute;
    left: 470px;
    top: 292px;
    display: flex;
    align-items: flex-start;
    gap: 22px;
    font-size: 17px;
    font-weight: 500;
    line-height: 1.45;
    white-space: nowrap;
  }
  .contact-address address { font-style: normal; }
  .icon { flex: none; }

  .brand {
    position: absolute;
    right: 70px;
    top: 168px;
    display: flex;
    align-items: center;
    gap: 20px;
  }
  .brand__dot {
    width: 46px;
    height: 46px;
    border-radius: 50%;
    background: var(--brand-green);
  }
  .brand__name {
    font-size: 46px;
    font-weight: 700;
    color: var(--brand-blue);
    letter-spacing: -0.5px;
    white-space: nowrap;
  }
</style>
</head>
<body>

  <section class="card card--front" aria-label="Business card front">
    <svg class="card__bands" viewBox="0 0 840 480" aria-hidden="true">
      <rect x="0" y="0" width="300" height="6" fill="var(--brand-blue)"/>
      <rect x="300" y="0" width="540" height="6" fill="var(--brand-green)"/>
      <polygon points="0,150 260,150 290,176 0,176" fill="var(--brand-blue)"/>
      <polygon points="420,212 840,212 840,240 460,240" fill="var(--brand-green)"/>
      <rect x="0" y="474" width="300" height="6" fill="var(--brand-blue)"/>
      <rect x="300" y="474" width="540" height="6" fill="var(--brand-green)"/>
    </svg>

    <h1 class="contact-name">Dana Merrow</h1>
    <p class="contact-title">Founder/CEO</p>

    <p class="contact-email">
      <svg class="icon" width="34" height="24" viewBox="0 0 34 24" aria-hidden="true">
        <rect x="1.5" y="1.5" width="31" height="21" fill="none" stroke="var(--ink)" stroke-width="2"/>
        <polyline points="1.5,1.5 17,14 32.5,1.5" fill="none" stroke="var(--ink)" stroke-width="2"/>
        <line x1="1.5" y1="22.5" x2="13" y2="11" stroke="var(--ink)" stroke-width="2"/>
        <line x1="32.5" y1="22.5" x2="21" y2="11" stroke="var(--ink)" stroke-width="2"/>
      </svg>
      dana@quillmarkledger.example
    </p>

    <div class="contact-address">
      <svg class="icon" width="30" height="36" viewBox="0 0 30 36" aria-hidden="true">
        <path d="M15 2 C8 2 4 7 4 12 C4 19 15 28 15 28 C15 28 26 19 26 12 C26 7 22 2 15 2 Z" fill="none" stroke="var(--ink)" stroke-width="2"/>
        <circle cx="15" cy="12" r="4" fill="none" stroke="var(--ink)" stroke-width="2"/>
        <polyline points="9,26 2,34 28,34 21,26" fill="none" stroke="var(--ink)" stroke-width="2"/>
      </svg>
      <address>
        2740 Harlow Avenue<br>
        Boston MA 02135<br>
        (617)555-0194
      </address>
    </div>
  </section>

  <section class="card card--back" aria-label="Business card back">
    <svg class="card__bands" viewBox="0 0 840 480" aria-hidden="true">
      <rect x="0" y="0" width="300" height="6" fill="var(--brand-blue)"/>
      <rect x="300" y="0" width="540" height="6" fill="var(--brand-green)"/>
      <polygon points="0,292 260,292 290,320 0,320" fill="var(--brand-blue)"/>
      <polygon points="300,348 840,348 840,380 340,380" fill="var(--brand-green)"/>
      <rect x="0" y="474" width="300" height="6" fill="var(--brand-blue)"/>
      <rect x="300" y="474" width="540" height="6" fill="var(--brand-green)"/>
    </svg>

    <div class="brand">
      <span class="brand__dot" aria-hidden="true"></span>
      <span class="brand__name">Quillmark Ledger</span>
    </div>
  </section>

</body>
</html>
```